Buch-/eBook-Cover für ein Fantasy Roman
Zielgruppe
Meine Zielgruppe sind Jugendliche und junge Erwachsene, aber auch für Ältere könnte mein Buch interessant sein.
Aufgabenstellung
Bei meinem Buch handelt es sich um einen Fantasy Roman. Es heißt 'Nachtfalter - Wahrheit braucht ihre Zeit' und der Autor ist Mara Oswaldtinger.
Das Buch handelt von einem Mädchen, welches eigentlich ein ganz normales Leben führt, aber dieses durch eine Pressekonferenz vom Präsidenten komplett durcheinander gerät. Denn viele Menschen sollen an einem Virus leiden. Die Menschen sollen sich aber keine Sorgen machen. Doch alles läuft durcheinander, da die infizierten Menschen einer nach dem anderen spurlos verschwinden.
Auf meinem Cover soll keine Figur zu sehen sein. Ich hätte gerne ein Zusammenspiel zwischen den Farben Blau und Grün. sie sollen harmonisch und fließend ineinander übergehen. Auch etwas Glitzer für etwas Geheimnisvolles darf auf dem Cover sein. Den Titel hätte ich gerne in der Mitte. Wo der Autorname stehen soll, bin ich offen.

```html
<!DOCTYPE html>
<html lang="de">
<head>
<meta charset="utf-8">
<title>Nachtfalter – Buchcover</title>
<link rel="stylesheet" href="https://fonts.googleapis.com/css2?family=Josefin+Sans:wght@400&family=Playfair+Display:wght@400;500&family=Yellowtail&display=swap">
<style>
  :root {
    --stage: #e2e2e2;
    --ink: #ffffff;
    --deep: #123f52;
    --teal: #1b6f73;
    --glow: #4f9a8e;
    --mist: #2e8584;
    --shadow-blue: #0f3547;
  }
  * { margin: 0; padding: 0; box-sizing: border-box; }
  html, body {
    width: 1200px;
    height: 857px;
    overflow: hidden;
    background: var(--stage);
  }
  .cover {
    position: absolute;
    left: 339px;
    top: 36px;
    width: 522px;
    height: 785px;
    overflow: hidden;
    color: var(--ink);
  }
  .cover-art {
    position: absolute;
    inset: 0;
    background:
      radial-gradient(ellipse 38% 22% at 52% 28%, rgba(120,170,150,0.45), transparent 70%),
      radial-gradient(ellipse 30% 40% at 48% 55%, rgba(79,154,142,0.55), transparent 75%),
      radial-gradient(ellipse 40% 30% at 85% 12%, rgba(46,133,132,0.6), transparent 70%),
      radial-gradient(ellipse 35% 30% at 12% 60%, rgba(60,130,110,0.45), transparent 70%),
      radial-gradient(ellipse 60% 30% at 50% 95%, rgba(15,53,71,0.9), transparent 80%),
      linear-gradient(160deg, var(--deep) 0%, var(--teal) 40%, var(--mist) 55%, var(--shadow-blue) 100%);
  }
  .author {
    position: absolute;
    top: 99px;
    left: 0;
    width: 100%;
    text-align: center;
    font-family: "Josefin Sans", sans-serif;
    font-size: 25px;
    letter-spacing: 1.5px;
    text-transform: uppercase;
  }
  .title {
    position: absolute;
    top: 208px;
    left: 0;
    width: 100%;
    text-align: center;
    font-family: "Playfair Display", serif;
    font-weight: 500;
    line-height: 1;
    white-space: nowrap;
  }
  .title-initial { font-size: 104px; }
  .title-rest { font-size: 58px; text-transform: uppercase; letter-spacing: -0.5px; }
  .subtitle {
    position: absolute;
    top: 362px;
    left: 0;
    width: 100%;
    text-align: center;
    font-family: "Yellowtail", cursive;
    font-size: 80px;
    line-height: 73px;
  }
  .subtitle span { display: block; }
</style>
</head>
<body>
  <main class="cover">
    <div class="cover-art" role="img" aria-label="Abstrakte, fließende Rauch- und Wasserstruktur in Blau- und Grüntönen mit leichtem Schimmer"></div>
    <p class="author">Mara Oswaldtinger</p>
    <h1 class="title"><span class="title-initial">N</span><span class="title-rest">achtfalter</span></h1>
    <p class="subtitle">
      <span>Wahrheit</span>
      <span>braucht</span>
      <span>ihre</span>
      <span>Zeit</span>
    </p>
  </main>
</body>
</html>
```